New Business Card

Would like a shiny card with Metallic logo raised on th front. Address 418 Kestwick Lane, Toronto Ontario M4T2B8, phone 416 555 0382, email kmvc@lorentel.ca and web www.kmvc.ca on the back in right and left lower corners balanced. Top of back should say Attentive Care for Pets and the Families Who Love Them centered. Leaving space on the back to write. Horizontal placement

```html
<!DOCTYPE html>
<html lang="en">
<head>
<meta charset="utf-8">
<title>Kestwick Meadow Animal Hospital – Business Card</title>
<link href="https://fonts.googleapis.com/css2?family=Roboto:wght@400;500;700&display=swap" rel="stylesheet">
<style>
  :root {
    --backdrop: #3a302b;
    --silver-light: #f4f4f4;
    --silver-mid: #c9c9c9;
    --silver-dark: #8d8d8d;
    --ink: #1f1f1f;
    --ink-soft: #3c3c3c;
    --paper: #ffffff;
    --rule: #b9b9b9;
    --tagline: #555555;
  }
  * { margin: 0; padding: 0; box-sizing: border-box; }
  html, body { width: 1200px; height: 769px; overflow: hidden; }
  body {
    background: var(--backdrop);
    font-family: "Roboto", Arial, sans-serif;
    display: flex;
    align-items: center;
    justify-content: center;
    gap: 40px;
  }
  .card {
    position: relative;
    width: 540px;
    height: 309px;
    border-radius: 3px;
    box-shadow: 0 12px 30px rgba(0,0,0,0.45);
    overflow: hidden;
  }
  .card--front {
    background: radial-gradient(ellipse 75% 90% at 48% 35%, var(--silver-light) 0%, var(--silver-mid) 55%, var(--silver-dark) 100%);
  }
  .brand {
    position: absolute;
    left: 34px;
    top: 40px;
    display: flex;
    align-items: center;
    gap: 12px;
  }
  .brand__dot {
    width: 14px; height: 14px;
    border-radius: 50%;
    background: var(--ink-soft);
    flex: none;
  }
  .brand__name {
    font-weight: 700;
    font-size: 21px;
    letter-spacing: 0.5px;
    text-transform: uppercase;
    color: var(--ink-soft);
    line-height: 1.15;
  }
  .person {
    position: absolute;
    left: 34px;
    top: 130px;
    color: var(--ink);
  }
  .person__name { font-weight: 700; font-size: 17px; text-transform: uppercase; }
  .person__title { font-size: 13px; text-transform: uppercase; margin-top: 3px; }
  .contact {
    position: absolute;
    right: 36px;
    bottom: 30px;
    font-size: 14px;
    color: var(--ink);
    line-height: 1.35;
  }
  .contact__address { margin-bottom: 4px; }
  .contact__row { display: flex; align-items: center; gap: 8px; }
  .contact__row svg { width: 11px; height: 11px; fill: var(--ink); flex: none; }
  .card--back { background: var(--paper); }
  .tagline {
    position: absolute;
    top: 30px;
    left: 0; right: 0;
    text-align: center;
    font-size: 15px;
    font-weight: 500;
    color: var(--tagline);
  }
  .write-line {
    position: absolute;
    left: 34px; right: 34px;
    height: 1px;
    background: var(--rule);
  }
</style>
</head>
<body>
  <section class="card card--front">
    <div class="brand">
      <span class="brand__dot"></span>
      <span class="brand__name">Kestwick Meadow<br>Animal Hospital</span>
    </div>
    <div class="person">
      <p class="person__name">Jordan Pell</p>
      <p class="person__title">CEO/Founder</p>
    </div>
    <div class="contact">
      <p class="contact__address">418 Kestwick Lane<br>Toronto Ontario M4T2B8</p>
      <p class="contact__row">
        <svg viewBox="0 0 24 24"><path d="M6.6 10.8a15 15 0 0 0 6.6 6.6l2.2-2.2c.3-.3.7-.4 1-.2 1.1.4 2.3.6 3.6.6.6 0 1 .4 1 1V20c0 .6-.4 1-1 1A17 17 0 0 1 3 4c0-.6.4-1 1-1h3.5c.6 0 1 .4 1 1 0 1.3.2 2.5.6 3.6.1.3 0 .7-.2 1z"/></svg>
        416 555 0382
      </p>
      <p class="contact__row">
        <svg viewBox="0 0 24 24"><path d="M2 5h20v14H2z M2 5l10 8 10-8" fill="none" stroke="#1f1f1f" stroke-width="2.4"/></svg>
        kmvc@lorentel.ca
      </p>
      <p class="contact__row">
        <svg viewBox="0 0 24 24"><circle cx="12" cy="12" r="10"/></svg>
        www.kmvc.ca
      </p>
    </div>
  </section>

  <section class="card card--back">
    <p class="tagline">Attentive Care for Pets and the Families Who Love Them</p>
    <div class="write-line" style="top:78px"></div>
    <div class="write-line" style="top:132px"></div>
    <div class="write-line" style="top:186px"></div>
    <div class="write-line" style="top:240px"></div>
  </section>
</body>
</html>
```